NIGHTCLUB POSTER DESIGN

We are an established (2002) nightclub in Calgary, Canada looking to freshen up and re-brand our Friday nights.
We cater primarily to the college crowd, however would like to maintain an image that is not too young/messy as we also have a corporate crowd that we need to stay appealing to.
We are edgy, sexy, fun, friendly, relevant, high energy, synonymous with having a wild night out with friends.
Our venue is very comfortable, not pretentious, is wood and brick and hosts over 3000 guests a weekend.
We are always cutting edge and ahead of our competitors in our market - so please no boring, seen it a million times nightclub posters...you know the ones :)
We want the imagery to evoke a "feel good" emotion, something people won't forget, that will catch attention, that we can keep for the next 10 years.

We are branding this night GLOW FRIDAY.
We would like this Friday night branding poster to read
The Timberyard (logo - attached) presents GLOW FRIDAYS.
GLOW FRIDAYS should be presented in such a way that we could use it as a stand alone logo for stickers, tattoos, etc.

This poster MUST READ:
"The Timberyard (logo) presents GLOW FRIDAYS.
Fishbowls $14 (4 oz.)
Featuring DJKrumble & DJ Velmo Q.

I have attached a few looks that we have liked.
Updates

This poster must read "The Timberyard (logo) presents GLOW FRIDAYS.
This is how we will be branding our Friday's forever so there is no date.

Hi everyone!
Thank you for your submissions.
These are unfortunately not what I was looking for. We need to be sexy, edgy, high energy, nightclub posters.
There will have to be some sort of image please.
Thank you & good luck!

Target Market(s)

18-30

Industry/Entity Type

College

Requirements
Nice to have
• We want to appeal to women more than men.
We'd like it to be fairly clean, eye catching and easy to read.
Should not have
• Nothing too offensive (the Unfiltered Sunday image is as offensive as we'll go and that matches our "Unfiltered" branding.

```html
<!DOCTYPE html>
<html lang="en">
<head>
<meta charset="utf-8">
<title>The Timberyard presents Glow Fridays</title>
<link rel="stylesheet" href="https://fonts.googleapis.com/css2?family=Archivo+Black&family=Fira+Sans+Extra+Condensed:wght@400;800&display=swap">
<style>
  :root {
    --navy-deep: #0b1c42;
    --navy: #173a78;
    --blue-light: #3d72b8;
    --cyan-line: #8fe3ff;
    --silver: #e4eaee;
    --silver-dark: #8a959e;
    --yellow: #f3e41c;
    --gold-light: #f6d46a;
    --gold: #d3a02a;
    --gold-dark: #7a5410;
    --ink: #262a30;
    --white: #ffffff;
  }
  * { margin: 0; padding: 0; box-sizing: border-box; }
  html, body { width: 816px; height: 1200px; overflow: hidden; background: var(--navy-deep); }
  .poster {
    position: relative;
    width: 816px; height: 1200px; overflow: hidden;
    background:
      radial-gradient(ellipse 60% 45% at 52% 52%, var(--blue-light) 0%, rgba(61,114,184,0) 70%),
      linear-gradient(180deg, var(--navy-deep) 0%, var(--navy) 30%, var(--navy) 70%, var(--navy-deep) 100%);
    font-family: "Archivo Black", "Arial Black", sans-serif;
  }
  .shapes { position: absolute; inset: 0; }
  .venue-name {
    position: absolute; left: 0; right: 0; top: 70px;
    text-align: center; font-size: 62px; color: var(--silver);
    letter-spacing: 1px; text-transform: uppercase;
  }
  .presents {
    position: absolute; left: 0; right: 0; top: 220px;
    text-align: center; font-size: 30px; color: var(--yellow);
    letter-spacing: 0.5px;
  }
  .night-title { position: absolute; inset: 0; }
  .night-title span {
    position: absolute; display: block; white-space: nowrap;
    background: linear-gradient(180deg, #ffffff 0%, var(--silver) 45%, var(--silver-dark) 55%, #f2f5f7 100%);
    -webkit-background-clip: text; background-clip: text; color: transparent;
    filter: drop-shadow(3px 5px 2px rgba(40,30,5,0.65));
  }
  .night-title .word-glow { left: 190px; top: 410px; font-size: 140px; transform: rotate(-6deg); }
  .night-title .word-fridays { left: 84px; top: 560px; font-size: 158px; letter-spacing: -4px; transform: rotate(-9deg); transform-origin: left bottom; }
  .drink-offer {
    position: absolute; left: 113px; top: 839px; width: 608px; height: 81px;
    border-radius: 6px;
    background: linear-gradient(180deg, var(--gold-light) 0%, var(--gold) 55%, var(--gold-dark) 100%);
    box-shadow: 0 4px 10px rgba(0,0,0,0.5), inset 0 0 0 2px rgba(255,230,150,0.6);
    display: flex; align-items: center; justify-content: center;
    font-size: 40px; color: var(--ink); letter-spacing: -1px;
  }
  .featuring {
    position: absolute; left: 200px; top: 1026px;
    font-family: "Fira Sans Extra Condensed", "Arial Narrow", sans-serif;
    font-weight: 400; font-size: 22px; color: var(--white); letter-spacing: 1px;
  }
  .dj-lineup {
    position: absolute; left: 0; right: 0; top: 1056px;
    text-align: center;
    font-family: "Fira Sans Extra Condensed", "Arial Narrow", sans-serif;
    font-weight: 800; font-size: 70px; color: var(--white); letter-spacing: 3px;
    text-shadow: 0 3px 4px rgba(0,0,0,0.5);
  }
</style>
</head>
<body>
<main class="poster">
  <svg class="shapes" width="816" height="1200" viewBox="0 0 816 1200" aria-hidden="true">
    <defs>
      <linearGradient id="triangle-fill" x1="0" y1="0" x2="1" y2="1">
        <stop offset="0" stop-color="#bfe3ff"/>
        <stop offset="0.5" stop-color="#5aa6ea"/>
        <stop offset="1" stop-color="#2e6fbf"/>
      </linearGradient>
      <linearGradient id="plate-fill" x1="0" y1="0" x2="0.3" y2="1">
        <stop offset="0" stop-color="#e9bf4a"/>
        <stop offset="0.5" stop-color="#c48f1f"/>
        <stop offset="1" stop-color="#6e4a0c"/>
      </linearGradient>
      <radialGradient id="splash-fill" cx="0.5" cy="0.5" r="0.5">
        <stop offset="0" stop-color="#fff6d0" stop-opacity="0.85"/>
        <stop offset="0.6" stop-color="#cfe6f7" stop-opacity="0.35"/>
        <stop offset="1" stop-color="#cfe6f7" stop-opacity="0"/>
      </radialGradient>
    </defs>
    <path class="frame-top" d="M134 80 V200 Q134 212 146 213 L816 224" fill="none" stroke="var(--cyan-line)" stroke-width="3"/>
    <path class="frame-bottom" d="M136 952 H735 Q739 952 739 946 V843" fill="none" stroke="var(--cyan-line)" stroke-width="3"/>
    <path class="frame-offer" d="M100 898 V832 Q100 825 108 825 H716" fill="none" stroke="#ffffff" stroke-width="3" opacity="0.9"/>
    <path class="emblem-triangle" d="M212 262 Q220 250 232 262 L490 580 L145 470 Z" fill="url(#triangle-fill)"/>
    <path class="emblem-plate" d="M54 485 L470 400 L703 445 L640 790 L260 790 L110 700 Z" fill="url(#plate-fill)"/>
    <ellipse role="img" aria-label="Splash of water droplets around the title" cx="420" cy="780" rx="360" ry="80" fill="url(#splash-fill)"/>
    <line class="rule-left" x1="0" y1="1040" x2="190" y2="1040" stroke="#ffffff" stroke-width="1.5" opacity="0.8"/>
    <line class="rule-right" x1="336" y1="1040" x2="816" y2="1040" stroke="#ffffff" stroke-width="1.5" opacity="0.8"/>
  </svg>

  <h1 class="venue-name">The Timberyard</h1>
  <p class="presents">PRESENTS</p>

  <h2 class="night-title">
    <span class="word-glow">GLOW</span>
    <span class="word-fridays">FRIDAYS</span>
  </h2>

  <p class="drink-offer">FISHBOWLS $14 (4 OZ.)</p>

  <p class="featuring">FEATURING</p>
  <p class="dj-lineup">DJKRUMBLE &amp; DJ VELMO Q.</p>
</main>
</body>
</html>
```